Label Design Project for my tea product Imported from Japan

I have a tea importing business. I want someone to help me design a label for my Uji matcha tea product. I want the label to be modern, neat, and beautifully designed. I prefer it to be easily adaptable to other tea products that I will be importing.
Product name: Organic Uji Matcha
Company name: Calm Harbor Leaf Merchants
Description: Powdered Green Tea Matcha
Ceremonial grade premium quality
Directly imported from Japan
This product is going to be sold in the U.S. market, so please make sure that the label is in compliance with the FDA regulations.

Target Market(s)

High end tea consumers

Industry/Entity Type

Business

Requirements
Must have
• Marking of origin : product of Japan
• Imported by: Calm Harbor Leaf Merchants
• Leave space for Net weight, the name and place of business of the manufacturer.
• Ingredients: Green Tea 100%
• Nutrition list is not necessary.

```html
<!DOCTYPE html>
<html lang="en">
<head>
<meta charset="UTF-8">
<title>Organic Uji Matcha – Product Label</title>
<link href="https://fonts.googleapis.com/css2?family=Kaushan+Script&family=Open+Sans:wght@400;600&family=Archivo+Narrow:wght@400&display=swap" rel="stylesheet">
<style>
  :root {
    --page-bg: #ffffff;
    --label-yellow: #f8ee0a;
    --label-lime: #c3dc2c;
    --label-green: #8cc63f;
    --label-border: #3a3a3a;
    --ink: #111111;
    --ink-soft: #2a2a2a;
    --muted: #6a6a78;
    --ring-purple: #6a3c96;
    --ring-lime: #b5d63a;
  }
  * { margin: 0; padding: 0; box-sizing: border-box; }
  html, body {
    width: 1200px;
    height: 1000px;
    overflow: hidden;
    background: var(--page-bg);
  }
  .canvas {
    position: relative;
    width: 1200px;
    height: 1000px;
  }
  .label {
    position: absolute;
    left: 369px;
    top: 88px;
    width: 504px;
    height: 833px;
    border: 1px solid var(--label-border);
    background: linear-gradient(160deg, var(--label-yellow) 0%, var(--label-lime) 38%, var(--label-green) 100%);
    font-family: "Open Sans", sans-serif;
    color: var(--ink);
  }
  .importer {
    position: absolute;
    left: 0;
    top: 62px;
    width: 100%;
  }
  .importer-lead {
    position: absolute;
    left: 239px;
    top: 0;
    font-size: 24px;
    font-weight: 400;
    letter-spacing: 0.3px;
    color: var(--ink-soft);
  }
  .importer-name {
    position: absolute;
    left: 0;
    top: 46px;
    width: 100%;
    text-align: center;
    font-size: 22px;
    font-weight: 400;
    letter-spacing: 0.5px;
    color: var(--muted);
  }
  .product-name {
    position: absolute;
    left: 0;
    top: 170px;
    width: 100%;
    text-align: center;
    font-family: "Kaushan Script", cursive;
    font-size: 52px;
    line-height: 1;
    color: var(--ink);
  }
  .product-grade {
    position: absolute;
    left: 0;
    top: 242px;
    width: 100%;
    text-align: center;
    font-size: 19px;
    font-weight: 600;
    color: var(--muted);
  }
  .hero-art {
    position: absolute;
    left: 42px;
    top: 277px;
    width: 424px;
    height: 382px;
  }
  .facts {
    position: absolute;
    left: 0;
    top: 662px;
    width: 100%;
    text-align: center;
    line-height: 1;
  }
  .net-weight {
    font-family: "Archivo Narrow", sans-serif;
    font-size: 23px;
    transform: scaleX(0.88);
  }
  .ingredients {
    margin-top: 4px;
    font-size: 16.5px;
  }
  .origin {
    margin-top: 7px;
    font-size: 21px;
    letter-spacing: 1.1px;
  }
  .manufacturer {
    position: absolute;
    left: 41px;
    top: 754px;
    font-size: 16px;
    letter-spacing: 0.6px;
    line-height: 22px;
    color: var(--ink-soft);
  }
</style>
</head>
<body>
<div class="canvas">
  <section class="label">
    <div class="importer">
      <p class="importer-lead">Imported By</p>
      <p class="importer-name">Calm Harbor Leaf Merchants</p>
    </div>

    <h1 class="product-name">Organic Uji Matcha</h1>
    <p class="product-grade">Ceremonial Grade Premium Quality</p>

    <svg class="hero-art" viewBox="0 0 424 382" role="img" aria-label="Decorative lattice ring framing a photograph of a cup of green tea on a saucer with mint leaves">
      <defs>
        <radialGradient id="heroFill" cx="50%" cy="50%" r="50%">
          <stop offset="0%" stop-color="#ffffff"/>
          <stop offset="70%" stop-color="#ffffff"/>
          <stop offset="84%" stop-color="#d8e7a0"/>
          <stop offset="100%" stop-color="#a58cc4"/>
        </radialGradient>
      </defs>
      <ellipse cx="212" cy="191" rx="212" ry="191" fill="url(#heroFill)"/>
    </svg>

    <div class="facts">
      <p class="net-weight">Net weight: xxx xx</p>
      <p class="ingredients">Ingredients: Green Tea 100%</p>
      <p class="origin">Directly Imported From Japan</p>
    </div>

    <div class="manufacturer">
      <p>Manufactured By: xxxxxxx</p>
      <p>Address: xxxxxxx</p>
    </div>
  </section>
</div>
</body>
</html>
```